Vintrel.com- International Goal Achievement Coach Needs Website Design

I need a web design for my new company called Vintrel. I help people who are stuck, people who have a big dream, but don't know how to get there. I help them to break their dreams down into small, manageable steps... and then I'm the "kick in the shin" to get them moving and thriving!

We can all be better- We can all DO better. I inspire people to Ride Onward in the direction of your dreams.

I have uploaded my logo along with some vintage champagne posters. Please use the vintage posters as inspiration. I like the bold, vintage look and feel. I would love the main colors of the design to be black, white and metallic gold. And to follow along this vintage look and feel. Please feel free to use the logo in black or metallic gold or white.

Target Market(s)

websites that I like- janetrulsby.com & hollyp.tv

I would like to also use the vintage champagne photos attached as inspiration as well.

Industry/Entity Type

It Company

Requirements
Must have
• Tabs should include: About, Work With Me, Praise, Giving Back

On the homepage add:
* Sign up for newsletter with space to enter name and email (No click throughs)
* Upcoming Events/Sessions
* Newsletter Posts
* Resources
* Praise Section

* Large photo on top with additional photos throughout the page/site.
Nice to have
• Any additions you can bring to the table would be greatly appreciated.

```html
<!DOCTYPE html>
<html lang="en">
<head>
<meta charset="utf-8">
<title>Vintrel – Goal Achievement Coach</title>
<link href="https://fonts.googleapis.com/css2?family=Source+Sans+3:wght@300;400&display=swap" rel="stylesheet">
<style>
  :root{
    --gold:#a97e57;
    --navy:#2d3a4b;
    --ink:#222;
    --muted:#777;
    --footer:#f1f1f1;
    --white:#fff;
  }
  *{margin:0;padding:0;box-sizing:border-box}
  html,body{width:900px;height:1200px;overflow:hidden;background:var(--white)}
  body{position:relative;font-family:"Source Sans 3",sans-serif;font-weight:300;color:var(--ink)}
  .abs{position:absolute}

  .brand{display:flex;align-items:center;gap:12px}
  .brand-mark{width:52px;height:52px;border-radius:50%;background:var(--gold)}
  .brand-name{font-size:30px;color:var(--gold);font-weight:400}

  .site-header{left:0;top:0;width:900px;height:94px}
  .site-header .brand{position:absolute;left:45px;top:21px}
  .nav{position:absolute;right:42px;top:34px;display:flex;gap:22px}
  .nav a{font-size:18px;color:var(--gold);text-decoration:none;position:relative}
  .nav a.active::before{content:"";position:absolute;left:0;right:0;top:-34px;height:6px;background:var(--gold)}

  .hero{left:0;top:94px;width:900px;height:388px;
    background:linear-gradient(100deg,#8f8b88 0%,#d8cbc2 30%,#e9e3dc 55%,#c9b7a4 80%,#a98f7a 100%)}
  .hero-panel{position:absolute;left:365px;top:161px;width:535px;height:143px;background:rgba(60,60,66,.78)}
  .hero-title{position:absolute;left:22px;top:14px;color:var(--white);font-size:47px;line-height:58px;font-weight:300}
  .hero-band{position:absolute;left:365px;top:304px;width:535px;height:38px;background:rgba(25,25,28,.9);
    color:var(--white);font-size:14px;padding:11px 26px;font-weight:300}

  .about{left:0;top:482px;width:900px;height:160px;background:var(--navy);color:var(--white)}
  .about h2{text-align:center;font-weight:300;font-size:24px;margin-top:18px}
  .about p{font-size:10px;line-height:17px;margin:12px 30px 0 36px}

  .feature{top:672px;width:202px}
  .feature h3{font-size:18px;font-weight:300;color:var(--gold);white-space:nowrap}
  .feature .photo{margin-top:12px;width:202px;height:117px}
  .feature p{margin-top:14px;font-size:10px;line-height:12.6px;color:var(--ink)}
  .feature .rule{position:absolute;top:260px;left:0;width:202px;height:1px;background:var(--gold)}
  .feature .more{position:absolute;top:253px;left:140px;width:47px;height:14px;background:var(--gold);
    color:var(--white);font-size:10px;text-align:center;line-height:14px}

  .site-footer{left:0;top:975px;width:900px;height:225px;background:var(--footer)}
  .site-footer .brand{position:absolute;left:45px;top:20px}
  .footer-rule{position:absolute;left:45px;top:87px;width:178px;height:1px;background:#d6d6d6}
  .contact{position:absolute;left:46px;top:94px;font-size:13px;line-height:20px;color:var(--ink);font-weight:300}
  .social{position:absolute;left:47px;top:160px;display:flex;gap:5px}
  .social span{width:22px;height:22px;border-radius:50%;background:#222}
  .footer-nav{position:absolute;left:282px;top:18px;width:132px}
  .footer-nav a{display:block;height:22px;margin-bottom:5.5px;padding-left:13px;line-height:22px;
    font-size:13px;color:var(--ink);text-decoration:none}
  .footer-nav a.active{background:var(--white);border-left:3px solid var(--gold);padding-left:10px}
  .signup{position:absolute;left:514px;top:22px;width:240px}
  .signup h4{font-size:17px;font-weight:300;color:var(--navy);margin-bottom:14px}
  .signup .field{width:233px;height:28px;background:var(--white);color:#999;font-size:13px;padding:6px 11px;margin-bottom:9px}
  .signup .btn{margin-left:2px;width:104px;height:27px;background:var(--navy);color:var(--white);font-size:13px;text-align:center;line-height:27px}
  .bottom-rule{position:absolute;left:45px;top:196px;width:818px;height:1px;background:#d0d0d0}
  .copyright{position:absolute;left:45px;top:202px;font-size:13px;color:var(--muted)}
  .privacy{position:absolute;right:37px;top:202px;font-size:13px;color:var(--muted)}
</style>
</head>
<body>

<header class="abs site-header">
  <div class="brand"><span class="brand-mark"></span><span class="brand-name">Vintrel</span></div>
  <nav class="nav">
    <a class="active" href="#">About</a>
    <a href="#">Work With Me</a>
    <a href="#">Praise</a>
    <a href="#">Giving Back</a>
  </nav>
</header>

<section class="abs hero" role="img" aria-label="Photo of a joyful woman in glasses raising her fists at her office desk">
  <div class="hero-panel">
    <h1 class="hero-title">BECOME THE happiest<br>PERSON YOU KNOW</h1>
  </div>
  <div class="hero-band">SIGN UP FOR TESSA'S NEW GUIDED MEDITATIONS AND VLOG. Its Free</div>
</section>

<section class="abs about">
  <h2>About Vintrel</h2>
  <p>Lorem Ipsum is simply dummy text of the printing and typesetting industry. Lorem Ipsum has been the industry's standard dummy text ever since the 1500s, when an unknown printer took a galley of type and scrambled it to make a type specimen book. It has survived Lorem Ipsum is simply dummy text of the printing and typesetting industry. Lorem Ipsum has been the industry's standard dummy text ever since the 1500s, when an unknown printer took a galley of type and scrambled it to make a type specimen book. It has survived Lorem Ipsum is simply dummy text of the printing and typesetting industry. Lorem Ipsum has been the industry's standard dummy text ever since the 1500s, when an unknown printer took a galley of type and printer took a galley of type and scrambled it to make a type specimen book. It has survived</p>
</section>

<article class="abs feature" style="left:36px">
  <h3>Upcoming Events/Sessions</h3>
  <div class="photo" role="img" aria-label="Photo of a man with arms raised in a sunlit field" style="background:linear-gradient(160deg,#d9b27c,#c89a68 50%,#9aa39c)"></div>
  <p>Lorem Ipsum is simply dummy text of the printing and typesetting industry. Lorem Ipsum has been the industry's standard dummy text ever since the 1500s, when an unknown printer took a galley of type and scrambled it to make a type specimen book. It has survived</p>
  <div class="rule"></div><div class="more">more</div>
</article>

<article class="abs feature" style="left:247px">
  <h3>Newsletter Posts</h3>
  <div class="photo" role="img" aria-label="Photo of a smiling team of business people" style="background:linear-gradient(180deg,#e6e6e6,#a9a9ac 60%,#55585e)"></div>
  <p>Lorem Ipsum is simply dummy text of the printing and typesetting industry. Lorem Ipsum has been the industry's standard dummy text ever since the 1500s, when an unknown printer took a galley of type and scrambled it to make a type specimen book. It has survived</p>
  <div class="rule"></div><div class="more">more</div>
</article>

<article class="abs feature" style="left:458px">
  <h3>Resources</h3>
  <div class="photo" role="img" aria-label="Photo of a mother and child in winter hats laughing" style="background:linear-gradient(135deg,#3f6f74,#b04a45 55%,#d69a5a)"></div>
  <p>Lorem Ipsum is simply dummy text of the printing and typesetting industry. Lorem Ipsum has been the industry's standard dummy text ever since the 1500s, when an unknown printer took a galley of type and scrambled it to make a type specimen book. It has survived</p>
  <div class="rule"></div><div class="more">more</div>
</article>

<article class="abs feature" style="left:669px">
  <h3>Praise Section</h3>
  <div class="photo" role="img" aria-label="Photo of a woman with open arms enjoying the sun" style="background:linear-gradient(90deg,#c9c9bb,#dcd5c6 50%,#a88b72)"></div>
  <p>Lorem Ipsum is simply dummy text of the printing and typesetting industry. Lorem Ipsum has been the industry's standard dummy text ever since the 1500s, when an unknown printer took a galley of type and scrambled it to make a type specimen book. It has survived</p>
  <div class="rule"></div><div class="more">more</div>
</article>

<footer class="abs site-footer">
  <div class="brand"><span class="brand-mark"></span><span class="brand-name">Vintrel</span></div>
  <div class="footer-rule"></div>
  <address class="contact" style="font-style:normal">42 Marlow Ct Fenwick,<br>OR 97402 541-555-0148<br>name@vintrel.com</address>
  <div class="social" aria-label="Social links"><span></span><span></span><span></span><span></span></div>
  <nav class="footer-nav">
    <a class="active" href="#">About</a>
    <a href="#">Work With Me</a>
    <a href="#">Praise</a>
    <a href="#">Giving Back</a>
    <a href="#">Contact Us</a>
  </nav>
  <div class="signup">
    <h4>Email News Letter</h4>
    <div class="field">Enter your name</div>
    <div class="field">Enter your Email</div>
    <div class="btn">Subscribe</div>
  </div>
  <div class="bottom-rule"></div>
  <div class="copyright">© 2014 vintrel.com</div>
  <div class="privacy">Privacy Policy</div>
</footer>

</body>
</html>
```